PV Hair and Beauty flyer

Hello I have hairdressing salon called PV Hair and Beauty.I need flyer with double side pls.On front side I need this picture to be there and under the pisture our full address,tel number and email address( 48 Fenwick rd E17 9QP 02074613398 media@pvhairandbeauty.co.uk). And under that shoud be written:Special offers
with 3 different discount squares at the bottom of the flyer.First visite 20% off,Second 15% off, thrd 10% off.At he other side of flyer should be following info:Ladies cut & blowdry with 3 different levels of stylist £45-£65,Gents cut £15-£36,Highlights from £45-£120,Express Blowdry £22-£35,Keratin tretmant £150,Manicure from £14,Pedicure from £25,Shellac from £28

```html
<!DOCTYPE html>
<html lang="en">
<head>
<meta charset="utf-8">
<title>PV Hair and Beauty – Flyer</title>
<link href="https://fonts.googleapis.com/css2?family=Questrial&family=Playfair+Display:ital@1&display=swap" rel="stylesheet">
<style>
  :root {
    --stage: #3b2a1f;
    --paper: #ffffff;
    --ink: #0d0d0d;
    --gold: #c9a56a;
    --gold-light: #e3c48f;
    --white: #ffffff;
    --rule: #8a8a8a;
  }
  * { box-sizing: border-box; margin: 0; padding: 0; }
  html, body { width: 1200px; height: 892px; overflow: hidden; }
  body { background: var(--stage); font-family: "Questrial", sans-serif; position: relative; }

  .side { position: absolute; top: 85px; height: 720px; width: 507px; }
  .side--front { left: 93px; background: var(--paper); }
  .side--back { left: 600px; background: var(--ink); }

  .brand {
    position: absolute; top: 45px; left: 0; width: 100%;
    display: flex; justify-content: center; align-items: center; gap: 10px;
    font-size: 27px; letter-spacing: 0.5px;
  }
  .brand__mark { width: 14px; height: 14px; background: var(--gold); }
  .side--front .brand { color: var(--ink); }
  .side--back .brand { color: var(--white); }

  .salon-photo {
    position: absolute; left: 19px; top: 101px; width: 468px; height: 375px;
    background: radial-gradient(ellipse at 50% 55%, #7a6259 0%, #4a3834 55%, #2a201e 100%);
  }
  .contact-bar {
    position: absolute; left: 19px; top: 476px; width: 468px; height: 28px;
    background: var(--ink); color: var(--white);
    display: flex; justify-content: center; align-items: center; gap: 6px;
    font-size: 13px; white-space: nowrap;
  }
  .contact-bar__sep { width: 6px; height: 6px; background: var(--white); display: inline-block; }

  .offers-ribbon { position: absolute; left: 115px; top: 512px; }
  .offers-ribbon__label {
    position: absolute; left: 20px; top: 4px; width: 236px; height: 38px;
    display: flex; align-items: center; justify-content: center;
    color: var(--white); font-size: 25px; letter-spacing: 0.5px; white-space: nowrap;
  }

  .offer {
    position: absolute; top: 577px; width: 115px; height: 118px;
    background: var(--ink); color: var(--gold);
  }
  .offer--first { left: 19px; }
  .offer--second { left: 196px; }
  .offer--third { left: 373px; }
  .offer__label {
    position: absolute; top: 12px; left: 6px; right: 6px;
    display: flex; align-items: center; gap: 4px;
    font-size: 8.5px; color: var(--gold-light); white-space: nowrap;
  }
  .offer__label::before, .offer__label::after { content: ""; flex: 1; height: 1px; background: var(--gold); }
  .offer__value {
    position: absolute; top: 26px; left: 8px;
    font-family: "Playfair Display", serif; font-style: italic;
    font-size: 62px; line-height: 1; color: var(--gold-light);
  }
  .offer__unit {
    position: absolute; top: 72px; left: 84px;
    font-family: "Playfair Display", serif; font-style: italic;
    font-size: 11px; color: var(--gold-light);
  }

  .price-list { position: absolute; top: 99px; left: 28px; width: 443px; list-style: none; }
  .price-list__item {
    height: 71px; border-bottom: 1px dotted var(--rule);
    display: flex; flex-direction: column; align-items: center;
  }
  .price-list__item:first-child { height: 60px; }
  .price-list__name {
    color: var(--gold); font-size: 15.5px; line-height: 20px; margin-top: 6px;
    white-space: nowrap;
  }
  .price-list__item:first-child .price-list__name { margin-top: 0; font-size: 14px; letter-spacing: -0.2px; }
  .price-list__price {
    background: var(--white); color: var(--ink);
    font-size: 24px; height: 36px; line-height: 36px; margin-top: 4px;
    padding: 0 10px; min-width: 100px; text-align: center; white-space: nowrap;
  }
  .price-list__item:first-child .price-list__price { margin-top: 2px; }

  .back-contact {
    position: absolute; top: 668px; left: 0; width: 100%;
    display: flex; justify-content: center; align-items: center; gap: 5px;
    color: var(--white); font-size: 12.5px; white-space: nowrap;
  }
  .back-contact .contact-bar__sep { width: 5px; height: 5px; }
</style>
</head>
<body>
  <section class="side side--front">
    <div class="brand"><span class="brand__mark"></span><span>PV HAIR AND BEAUTY</span></div>
    <div class="salon-photo" role="img" aria-label="Sepia group photo of the salon team posing together inside the salon"></div>
    <div class="contact-bar">
      <span>48 Fenwick rd E17 9QP</span><span class="contact-bar__sep"></span>
      <span>02074613398</span><span class="contact-bar__sep"></span>
      <span>media@pvhairandbeauty.co.uk</span>
    </div>
    <div class="offers-ribbon">
      <svg width="276" height="52" viewBox="0 0 276 52">
        <polygon points="0,14 24,14 24,46 0,46 10,30" fill="#c9a56a"/>
        <polygon points="276,14 252,14 252,46 276,46 266,30" fill="#c9a56a"/>
        <polygon points="20,42 28,50 28,42" fill="#9c7c48"/>
        <polygon points="256,42 248,50 248,42" fill="#9c7c48"/>
        <rect x="20" y="4" width="236" height="38" fill="#c9a56a"/>
      </svg>
      <div class="offers-ribbon__label">SPECIAL OFFERS</div>
    </div>
    <div class="offer offer--first"><div class="offer__label">FIRST VISIT</div><div class="offer__value">20</div><div class="offer__unit">%off</div></div>
    <div class="offer offer--second"><div class="offer__label">SECOND VISIT</div><div class="offer__value">15</div><div class="offer__unit">%off</div></div>
    <div class="offer offer--third"><div class="offer__label">THIRD VISIT</div><div class="offer__value">10</div><div class="offer__unit">%off</div></div>
  </section>

  <section class="side side--back">
    <div class="brand"><span class="brand__mark"></span><span>PV HAIR AND BEAUTY</span></div>
    <ul class="price-list">
      <li class="price-list__item"><span class="price-list__name">LADIES CUT &amp; BLOW-DRY WITH 3 DIFFERENT LEVELS OF STYLIST</span><span class="price-list__price">£45-£65</span></li>
      <li class="price-list__item"><span class="price-list__name">GENTS CUT</span><span class="price-list__price">£15-£36</span></li>
      <li class="price-list__item"><span class="price-list__name">HIGHLIGHTS FROM</span><span class="price-list__price">£45-£120</span></li>
      <li class="price-list__item"><span class="price-list__name">EXPRESS BLOW-DRY</span><span class="price-list__price">£22-£35</span></li>
      <li class="price-list__item"><span class="price-list__name">KERATIN TRETMANT</span><span class="price-list__price">£150</span></li>
      <li class="price-list__item"><span class="price-list__name">MANICURE FROM</span><span class="price-list__price">£14</span></li>
      <li class="price-list__item"><span class="price-list__name">PEDICURE FROM</span><span class="price-list__price">£25</span></li>
      <li class="price-list__item"><span class="price-list__name">SHELLAC FROM</span><span class="price-list__price">£28</span></li>
    </ul>
    <div class="back-contact">
      <span>48 Fenwick rd E17 9QP</span><span class="contact-bar__sep"></span>
      <span>02074613398</span><span class="contact-bar__sep"></span>
      <span>media@pvhairandbeauty.co.uk</span>
    </div>
  </section>
</body>
</html>
```